Business card for new consulting business - Brackenvale Enterprises Pty Ltd.

Consulting in the areas of Occupational Health, Safety and Community Relations in the resources (mining) industries. The consultant (me) will work both within Australia and overseas jurisdictions such as South East Asia, Africa , South America etc, often working with third world indigenous communities. The design should suggest a high level of social and environmental responsibility.

```html
<!DOCTYPE html>
<html lang="en">
<head>
<meta charset="utf-8">
<title>Brackenvale Enterprises – Business Card</title>
<link rel="stylesheet" href="https://fonts.googleapis.com/css2?family=Montserrat:wght@700;800&family=Roboto:wght@400;500&display=swap">
<style>
  :root {
    --page-bg: #e9ebee;
    --navy: #2b3590;
    --sky: #2aa3dd;
    --leaf: #3fa535;
    --leaf-light: #5cbf3e;
    --stripe-blue: #2f5bb5;
    --stripe-sky: #2c9ad6;
    --ink: #222;
    --name-red: #c0392b;
    --title-purple: #7b3fa0;
    --white: #fff;
  }
  * { box-sizing: border-box; margin: 0; padding: 0; }
  html, body { width: 1200px; height: 906px; overflow: hidden; }
  body {
    background: var(--page-bg);
    font-family: "Roboto", Arial, sans-serif;
    display: flex;
    flex-direction: column;
    align-items: center;
    justify-content: center;
    gap: 30px;
  }
  .card {
    width: 700px;
    height: 400px;
    border-radius: 26px;
    position: relative;
    overflow: hidden;
    box-shadow: 0 8px 24px rgba(0,0,0,.18);
  }

  /* Back side */
  .card-back {
    background: linear-gradient(30deg, var(--navy) 0%, #2f63b8 55%, var(--sky) 100%);
    color: var(--white);
  }
  .back-brand {
    position: absolute;
    top: 130px; left: 0; right: 0;
    display: flex; flex-direction: column; align-items: center; gap: 18px;
  }
  .brand-dot {
    width: 62px; height: 62px; border-radius: 50%;
    background: var(--white);
  }
  .back-brand .brand-name {
    font-family: "Montserrat", Arial, sans-serif;
    font-weight: 800;
    font-size: 30px;
    letter-spacing: .5px;
    text-align: center;
    line-height: 1.1;
  }
  .back-web {
    position: absolute; bottom: 44px; left: 0; right: 0;
    text-align: center;
    font-family: "Montserrat", Arial, sans-serif;
    font-weight: 700; font-size: 15px; letter-spacing: 1px;
  }

  /* Front side */
  .card-front { background: var(--white); }
  .waves { position: absolute; inset: 0; }
  .front-brand {
    position: absolute; left: 60px; top: 120px;
    display: flex; align-items: center; gap: 14px;
  }
  .front-brand .brand-dot { width: 44px; height: 44px; background: var(--leaf); }
  .front-brand .brand-name {
    font-family: "Montserrat", Arial, sans-serif;
    font-weight: 800; font-size: 27px; line-height: 1.1;
    color: var(--leaf);
  }
  .holder {
    position: absolute; right: 46px; top: 34px; text-align: right;
  }
  .holder-name {
    font-family: "Montserrat", Arial, sans-serif;
    font-weight: 800; font-size: 22px; color: var(--name-red); letter-spacing: .5px;
  }
  .holder-title {
    font-family: "Montserrat", Arial, sans-serif;
    font-weight: 700; font-size: 14px; color: var(--title-purple); margin-top: 2px;
  }
  .holder-address {
    font-size: 15px; color: var(--ink); margin-top: 10px; line-height: 1.35;
  }
  .contacts {
    position: absolute; right: 40px; bottom: 40px;
    list-style: none; color: var(--white); font-size: 17px; text-align: right;
  }
  .contacts li {
    display: flex; justify-content: flex-end; align-items: center; gap: 10px;
    line-height: 1.55;
  }
  .contacts svg { width: 16px; height: 16px; fill: var(--white); flex: none; }
</style>
</head>
<body>

  <section class="card card-back" aria-label="Card back">
    <div class="back-brand">
      <span class="brand-dot"></span>
      <div class="brand-name">BRACKENVALE<br>ENTERPRISES PTY LTD</div>
    </div>
    <div class="back-web">WWW.BRACKENVALE.COM</div>
  </section>

  <section class="card card-front" aria-label="Card front">
    <svg class="waves" viewBox="0 0 700 400" preserveAspectRatio="none" aria-hidden="true">
      <path d="M0,300 C180,305 330,290 440,200 C540,120 620,95 700,90 L700,140 C610,145 540,170 450,240 C340,320 180,320 0,315 Z" fill="var(--leaf-light)"/>
      <path d="M0,335 C190,335 340,320 455,240 C550,170 625,148 700,145 L700,170 C625,175 555,200 465,262 C350,342 190,352 0,352 Z" fill="var(--stripe-blue)"/>
      <path d="M0,358 C200,360 350,345 470,268 C560,208 630,185 700,178 L700,198 C630,206 565,228 478,288 C355,370 200,378 0,376 Z" fill="var(--stripe-sky)"/>
      <path d="M0,384 C210,386 360,370 485,292 C570,238 635,215 700,208 L700,400 L0,400 Z" fill="var(--leaf)"/>
    </svg>

    <div class="front-brand">
      <span class="brand-dot"></span>
      <div class="brand-name">BRACKENVALE<br>ENTERPRISES PTY LTD</div>
    </div>

    <div class="holder">
      <div class="holder-name">MARCUS ELLERY</div>
      <div class="holder-title">CEO/FOUNDER</div>
      <div class="holder-address">48 Kestrel Road<br>Suite 2, Orange, NSW 2800</div>
    </div>

    <ul class="contacts">
      <li>260.555.1842
        <svg viewBox="0 0 24 24"><path d="M6.6 10.8a15 15 0 0 0 6.6 6.6l2.2-2.2a1 1 0 0 1 1-.25 11 11 0 0 0 3.6.6 1 1 0 0 1 1 1V20a1 1 0 0 1-1 1A17 17 0 0 1 3 4a1 1 0 0 1 1-1h3.5a1 1 0 0 1 1 1c0 1.25.2 2.45.6 3.6a1 1 0 0 1-.25 1z"/></svg>
      </li>
      <li>260.555.1843
        <svg viewBox="0 0 24 24"><path d="M6 2h12v6H6zM4 9h16a2 2 0 0 1 2 2v6h-4v5H6v-5H2v-6a2 2 0 0 1 2-2zm4 8v3h8v-3z"/></svg>
      </li>
      <li>marcus@brackenvale.com
        <svg viewBox="0 0 24 24"><path d="M2 5h20v14H2zm2 2v.5l8 5 8-5V7zm0 2.8V17h16V9.8l-8 5z"/></svg>
      </li>
      <li>www.brackenvale.com
        <svg viewBox="0 0 24 24"><path d="M12 2a10 10 0 1 0 0 20 10 10 0 0 0 0-20zm6.9 6h-2.9a15 15 0 0 0-1.4-3.6A8 8 0 0 1 18.9 8zM12 4c.8 1.1 1.5 2.5 1.9 4h-3.8c.4-1.5 1.1-2.9 1.9-4zM4.3 14a8 8 0 0 1 0-4h3.4a16 16 0 0 0 0 4zm.8 2h2.9a15 15 0 0 0 1.4 3.6A8 8 0 0 1 5.1 16zM8 8H5.1a8 8 0 0 1 4.3-3.6A15 15 0 0 0 8 8zm4 12c-.8-1.1-1.5-2.5-1.9-4h3.8c-.4 1.5-1.1 2.9-1.9 4zm2.3-6H9.7a14 14 0 0 1 0-4h4.6a14 14 0 0 1 0 4zm.3 5.6A15 15 0 0 0 16 16h2.9a8 8 0 0 1-4.3 3.6zM16.3 14a16 16 0 0 0 0-4h3.4a8 8 0 0 1 0 4z"/></svg>
      </li>
    </ul>
  </section>

</body>
</html>
```